Car Waterless Cleaner 4 in 1 (100% Natural) Clean, Shine, Protect; Water Repellent. High Eff...

We need to design labels for our Car Care & Cleaning products,
Labels on both 500 ml Bottle Spray sides (text will be provided).
5 and 10 liters Car Shampoo.

I need you to come with Car necessary images (Shining cars, Leather car seats ...)

We are a manufacturer of innovative Green Cleaning products; made with green plants and grain extract, (Leather Cleaner & Conditioner, Multi purpuses Cleaner, Car Shine Polish, car Shampoo)

Target Market(s)

Car Care & Cleaning products, Car Dealer, Car Collectors.

Logo Text

No Idea yet, lol, ;) "Car Tovarex Plume" may be?

Font styles to use
Serif

Requirements
Must have
• Similar projects, Inoovative, Comprehencive, good expertise.

```html
<!DOCTYPE html>
<html lang="en">
<head>
<meta charset="UTF-8">
<title>Waterless Wash &amp; Polish – Spray Label</title>
<link rel="stylesheet" href="https://fonts.googleapis.com/css2?family=Montserrat:wght@700;800&family=Oswald:wght@500&family=Lato:wght@400;700;900&display=swap">
<style>
  :root {
    --page-bg: #f2f2f2;
    --label-dark: #1b1c1d;
    --label-dark-2: #2a2b2d;
    --logo-teal: #3f8c8c;
    --tab-red: #d7261e;
    --band-green-1: #5d7d32;
    --band-green-2: #46621f;
    --gold-1: #f6e27a;
    --gold-2: #c9972e;
    --gold-3: #a8781c;
    --text-light: #ffffff;
    --text-dark: #111111;
    --seal-brown: #6b3a1e;
    --seal-cream: #f4ecd8;
    --car-black: #0c0d0f;
    --car-body: #2b2e33;
    --car-chrome: #8a9098;
  }
  * { margin: 0; padding: 0; box-sizing: border-box; }
  html, body { width: 1200px; height: 2532px; overflow: hidden; }
  body { background: var(--page-bg); position: relative; }

  .label {
    position: absolute;
    left: 50px;
    top: 556px;
    width: 1100px;
    height: 1420px;
  }
  .label-shape { position: absolute; inset: 0; }

  .logo-placeholder {
    position: absolute;
    left: 194px;
    top: 222px;
    font-family: "Montserrat", sans-serif;
    font-weight: 800;
    font-size: 68px;
    line-height: 1.06;
    color: var(--logo-teal);
    letter-spacing: 1px;
  }

  .new-tab {
    position: absolute;
    right: 0;
    top: 246px;
    width: 270px;
    height: 94px;
    background: var(--tab-red);
    border-radius: 40px 0 0 40px;
    display: flex;
    align-items: center;
    justify-content: center;
    font-family: "Montserrat", sans-serif;
    font-weight: 800;
    font-size: 50px;
    color: var(--text-light);
  }

  .title-band {
    position: absolute;
    left: 0;
    top: 480px;
    width: 100%;
    height: 94px;
    background: linear-gradient(180deg, var(--band-green-1), var(--band-green-2));
    display: flex;
    align-items: center;
    justify-content: center;
  }
  .product-title {
    font-family: "Oswald", sans-serif;
    font-weight: 500;
    font-size: 68px;
    letter-spacing: 0.5px;
    background: linear-gradient(180deg, var(--gold-1) 10%, var(--gold-2) 70%, var(--gold-3));
    -webkit-background-clip: text;
    background-clip: text;
    color: transparent;
  }

  .benefits {
    position: absolute;
    left: 92px;
    top: 608px;
    list-style: none;
    font-family: "Lato", sans-serif;
    font-weight: 700;
    font-size: 31px;
    line-height: 47px;
    color: var(--text-light);
  }
  .benefits li { display: flex; align-items: center; gap: 14px; }
  .benefits svg { flex: none; }

  .car-photo {
    position: absolute;
    left: 20px;
    top: 830px;
    width: 1060px;
    height: 540px;
    border-radius: 120px 160px 40px 60px;
    background:
      radial-gradient(ellipse 38% 30% at 30% 52%, rgba(138,144,152,0.55), rgba(138,144,152,0) 100%),
      radial-gradient(ellipse 48% 42% at 55% 58%, var(--car-body) 0%, var(--car-black) 85%);
  }

  .guarantee-badge {
    position: absolute;
    left: 12px;
    top: 847px;
    width: 316px;
    height: 96px;
    border-radius: 16px 40px 40px 16px;
    background: linear-gradient(180deg, var(--gold-1), var(--gold-2));
    font-family: "Lato", sans-serif;
    font-weight: 900;
    font-size: 28px;
    line-height: 34px;
    color: var(--text-dark);
    text-align: center;
    display: flex;
    align-items: center;
    justify-content: center;
  }

  .natural-seal { position: absolute; left: 866px; top: 1194px; }

  .volume {
    position: absolute;
    right: 80px;
    bottom: 34px;
    font-family: "Lato", sans-serif;
    font-weight: 700;
    font-size: 34px;
    color: var(--text-light);
  }
</style>
</head>
<body>
  <main class="label">
    <svg class="label-shape" width="1100" height="1420" viewBox="0 0 1100 1420" aria-hidden="true">
      <defs>
        <linearGradient id="labelFill" x1="0" y1="0" x2="0" y2="1">
          <stop offset="0" stop-color="#2a2b2d"/>
          <stop offset="1" stop-color="#151617"/>
        </linearGradient>
      </defs>
      <path d="M0 175 C 320 70 700 0 1100 0 L1100 1420 L0 1420 Z" fill="url(#labelFill)"/>
    </svg>

    <div class="logo-placeholder">YOUR LOGO<br>GOES HERE</div>
    <div class="new-tab">NEW</div>

    <div class="title-band">
      <h1 class="product-title">WATERLESS WASH &amp; POLISH</h1>
    </div>

    <ul class="benefits">
      <li><svg width="22" height="24" viewBox="0 0 22 24"><path d="M0 0 L22 12 L0 24 Z" fill="#e0b43c"/></svg>Unmistakable showroom shine</li>
      <li><svg width="22" height="24" viewBox="0 0 22 24"><path d="M0 0 L22 12 L0 24 Z" fill="#e0b43c"/></svg>Repels dust and water spots</li>
      <li><svg width="22" height="24" viewBox="0 0 22 24"><path d="M0 0 L22 12 L0 24 Z" fill="#e0b43c"/></svg>No hazy film, swirls, or scratches left behind</li>
    </ul>

    <div class="car-photo" role="img" aria-label="Photo of a glossy black SUV in front three-quarter view with chrome highlights"></div>

    <div class="guarantee-badge">100% Results<br>Guaranteed!</div>

    <svg class="natural-seal" width="140" height="140" viewBox="0 0 140 140" aria-hidden="true">
      <circle cx="70" cy="70" r="68" fill="var(--seal-brown)"/>
      <circle cx="70" cy="70" r="50" fill="var(--seal-cream)"/>
    </svg>

    <div class="volume">500 ml</div>
  </main>
</body>
</html>
```